Steadfast Care - Need Stationary Design

We need a stationary pack for our new Care company based in the uk
Are corporate colours are Pink and purple
Please use attached logo
Target Market(s)
The Care Industry
Industry/Entity Type
It Company
Contact Information for Business Card
Melissa Rowden
Director

```html
<!DOCTYPE html>
<html lang="en">
<head>
<meta charset="utf-8">
<title>Steadfast Care — Letterhead</title>
<link rel="stylesheet" href="https://fonts.googleapis.com/css2?family=Arimo:wght@400&display=swap">
<style>
  :root {
    --pink: #e8389b;
    --purple: #8a4f9f;
    --wash: #f9f0f8;
    --ink: #222222;
    --frame: #3a3a3a;
    --paper: #ffffff;
  }
  * { box-sizing: border-box; margin: 0; padding: 0; }
  html, body { width: 847px; height: 1200px; overflow: hidden; background: var(--paper); }
  .letterhead {
    position: relative;
    width: 847px;
    height: 1200px;
    background: var(--paper);
    border: 1px solid var(--frame);
    overflow: hidden;
    font-family: "Arimo", Arial, Helvetica, sans-serif;
    color: var(--ink);
  }
  .backdrop { position: absolute; inset: 0; width: 847px; height: 1200px; }
  .backdrop path { fill: var(--wash); }

  .brand { position: absolute; left: 48px; top: 52px; width: 190px; }
  .brand-mark {
    display: block;
    width: 60px; height: 60px;
    margin-left: 74px;
    border-radius: 50%;
    background: var(--pink);
  }
  .brand-name {
    margin-top: 18px;
    font-size: 25px;
    line-height: 1;
    color: var(--purple);
    white-space: nowrap;
  }

  .contact { position: absolute; left: 537px; top: 54px; list-style: none; }
  .contact li {
    display: flex; align-items: center;
    height: 16px;
    font-size: 11px;
  }
  .contact svg { width: 14px; height: 12px; margin-right: 6px; fill: var(--pink); }

  .address { position: absolute; left: 716px; top: 56px; display: flex; }
  .address svg { width: 14px; height: 20px; fill: var(--pink); margin-right: 6px; }
  .address p { font-size: 11px; line-height: 15.5px; text-align: right; }
</style>
</head>
<body>
<main class="letterhead">
  <svg class="backdrop" viewBox="0 0 847 1200" aria-hidden="true">
    <path d="M288,0 C400,180 620,360 847,405 L847,495 C560,620 250,880 0,1185 C300,800 345,350 288,0 Z"/>
  </svg>

  <header class="brand">
    <span class="brand-mark" aria-hidden="true"></span>
    <p class="brand-name">Steadfast Care</p>
  </header>

  <ul class="contact">
    <li>
      <svg viewBox="0 0 14 12" aria-hidden="true"><path d="M1 5c0-3 3-4 6-4s6 1 6 4l-3 1-1-2H5L4 6 1 5zM3 7h8l1 4H2z"/></svg>
      01632 960482
    </li>
    <li>
      <svg viewBox="0 0 14 12" aria-hidden="true"><path d="M0 1h14v10H0zM1.5 2.5 7 7l5.5-4.5v1L7 8 1.5 3.5z" fill-rule="evenodd"/></svg>
      melissa@steadfastcare.com
    </li>
    <li>
      <svg viewBox="0 0 14 12" aria-hidden="true"><path d="M7 0a6 6 0 1 0 0 12A6 6 0 0 0 7 0zm0 1.2a4.8 4.8 0 1 1 0 9.6 4.8 4.8 0 0 1 0-9.6zM6.4 1.5h1.2v9H6.4zM2 5.4h10v1.2H2z"/></svg>
      www.steadfastcare.com
    </li>
  </ul>

  <div class="address">
    <svg viewBox="0 0 14 20" aria-hidden="true"><path d="M7 0a6 6 0 0 0-6 6c0 4.5 6 13 6 13s6-8.5 6-13a6 6 0 0 0-6-6zm0 3.2a2.8 2.8 0 1 1 0 5.6 2.8 2.8 0 0 1 0-5.6z" fill-rule="evenodd"/></svg>
    <p>address 1<br>address 2<br>address 3</p>
  </div>
</main>
</body>
</html>
```